Project Planning & Communication Process

Need a PowerPoint slide that illustrates our project planning and communication cycle. Our company has key meetings, and key communication vehicles (like emails and follow up tools) that we use to ensure our frontline staff are prepared to execute the new project successfully. This document needs to call out how the different components, like the meetings and emails, work together (like a flow chart), so someone who needs to use this process will understand what they should do. The slide needs to be simple yet comprehensive enough to guide someone through the details. I don't want it overwhelming. The primary focus is the process, not the details.

Use the color pallette included within the slide (shades of blue and gray, and black). This is for an insurance company (www.harborquill.com). Use this as a reference for the look and feel.

I have attached a sample slide of the flow chart process.

Click here if you cannot access the file. https://www.filecrate.example/s/q8wz2mbt7ypnc4r/Communcation_Methods_V1.pptx

If you are not able to see the uploaded slide.  Please send me your email address and I will send the slide to you directly. 

ISince I'm not able to upload the reference ppt file, 've uploaded the slide at FileCrate.  Please click here to access.
https://www.filecrate.example/s/q8wz2mbt7ypnc4r/Communcation_Methods_V1.pptx

Reason: extending one more day for designers to make last minute updates.

Target Market(s)

Vice Presidents and project managers/business partners within the organization.

Industry/Entity Type

Communication

Font styles to use
Sans Serif

Colors
3176b5

Requirements
Must have
• 1 page, color pallette assigned, be simple yet comprehensive. the focus needs to be on the process, not on the details.
Nice to have
• Doesn't have to follow the example I provided. Please feel free to approach from different ways.

```html
<!DOCTYPE html>
<html lang="en">
<head>
<meta charset="utf-8">
<title>Project Alignment &amp; Project Communication Process</title>
<link href="https://fonts.googleapis.com/css2?family=Titillium+Web:wght@400;700&family=Open+Sans:ital,wght@0,400;0,600;1,400&display=swap" rel="stylesheet">
<style>
  :root{
    --slate:#3a4150;
    --grey-ribbon:#c2c2c2;
    --grey-tab:#b0b0b0;
    --blue:#4f82c0;
    --blue-tab:#4a7dc0;
    --navy:#234472;
    --navy-tab:#1f3d69;
    --dot-blue:#3e6fb8;
    --dot-red:#e2504a;
    --panel-grey:#e4e4e4;
    --panel-blue:#4d7fbf;
    --panel-red:#e06858;
    --ink:#333;
    --label-blue:#3f6fb3;
    --white:#fff;
  }
  *{box-sizing:border-box;margin:0;padding:0}
  html,body{width:1200px;height:900px;overflow:hidden;background:var(--white)}
  body{position:relative;font-family:"Open Sans",Arial,sans-serif;color:var(--ink)}
  .header{position:absolute;left:0;top:0;width:1200px;height:83px;background:var(--slate);
    display:flex;align-items:center;justify-content:center}
  .header h1{font-family:"Titillium Web",Arial,sans-serif;font-weight:700;font-size:35px;color:var(--white);letter-spacing:.2px}
  .timeline{position:absolute;left:0;top:172px;width:1200px;border-top:3px dotted var(--dot-blue)}
  .milestone{position:absolute;top:147px;height:44px;width:94px;background:var(--white);
    border:3px dotted var(--dot-red);font-size:10px;display:flex;align-items:center;justify-content:center;color:var(--ink)}
  .icon{position:absolute;top:214px;width:56px;height:54px;border-radius:6px}
  .icon.grey{background:#d6d6d6}.icon.blue{background:#8fb0dc}.icon.navy{background:#6c84a8}
  .tab{position:absolute;top:290px;width:83px;height:21px;color:var(--white);font-family:"Titillium Web",Arial,sans-serif;
    font-style:italic;font-weight:700;font-size:21px;line-height:21px;text-align:center}
  .step{position:absolute;top:316px;width:83px;height:219px;color:var(--white);text-align:center;
    font-size:14px;line-height:18px;padding:22px 3px 0;
    clip-path:polygon(0 0,100% 0,100% 100%,50% 88%,0 100%)}
  .grey .tab,.tab.grey{background:var(--grey-tab)}
  .step.grey{background:var(--grey-ribbon)}
  .tab.blue{background:var(--blue-tab)} .step.blue{background:var(--blue)}
  .tab.navy{background:var(--navy-tab)} .step.navy{background:var(--navy)}
  .step .note{position:absolute;left:6px;right:4px;font-size:7.5px;line-height:10px;text-align:left}
  .step .star{color:var(--dot-red)}
  .step .mark{position:absolute;color:var(--dot-red);font-size:16px}
  .arrow{position:absolute;top:353px;width:22px;height:24px}
  .divider{position:absolute;left:0;top:691px;width:1200px;border-top:3px dotted var(--slate)}
  .notes{position:absolute;left:0;top:694px;width:670px;height:206px;background:var(--panel-grey);
    font-size:10.4px;line-height:13.5px;padding:5px 0 0 4px}
  .notes .item{margin-bottom:8.5px}
  .notes .label{color:var(--label-blue);font-weight:600}
  .notes .overview{padding-left:20px}
  .phases{position:absolute;left:670px;top:694px;width:375px;height:206px;background:var(--panel-blue)}
  .phase-icon{position:absolute;left:31px;width:62px;height:62px;border-radius:50%;background:var(--white);border:2px solid #2b3a52}
  .phase{position:absolute;left:80px;width:270px;height:48px;background:var(--white);
    clip-path:polygon(0 0,92% 0,100% 50%,92% 100%,0 100%);
    font-style:italic;font-size:15.5px;color:#222;display:flex;align-items:center;padding-left:33px}
  .legend{position:absolute;left:1045px;top:694px;width:155px;height:206px;background:var(--panel-red)}
  .key{position:absolute;left:20px;width:116px;height:28px;color:var(--white);font-size:13.5px;
    display:flex;align-items:center;justify-content:center;
    clip-path:polygon(0 0,100% 0,94% 50%,100% 100%,0 100%,6% 50%)}
  .key.meetings{top:70px;background:var(--blue)}
  .key.tools{top:106px;background:var(--navy)}
</style>
</head>
<body>
  <header class="header"><h1>Project Alignment &amp; Project Communication Process</h1></header>

  <div class="timeline"></div>
  <div class="milestone" style="left:135px">3+ Months Out</div>
  <div class="milestone" style="left:495px">2+ Months Out</div>
  <div class="milestone" style="left:729px">1 Month Out</div>
  <div class="milestone" style="left:850px">1 Week Out</div>

  <div class="icon grey" style="left:36px" role="img" aria-label="Lightbulb icon"></div>
  <div class="icon blue" style="left:155px" role="img" aria-label="Board meeting icon"></div>
  <div class="icon grey" style="left:274px" role="img" aria-label="Two people in discussion icon"></div>
  <div class="icon blue" style="left:393px" role="img" aria-label="Board meeting icon"></div>
  <div class="icon blue" style="left:512px" role="img" aria-label="Team hierarchy icon"></div>
  <div class="icon blue" style="left:632px" role="img" aria-label="Handshake icon"></div>
  <div class="icon blue" style="left:751px" role="img" aria-label="Team hierarchy icon"></div>
  <div class="icon navy" style="left:870px" role="img" aria-label="Group with memo icon"></div>
  <div class="icon navy" style="left:989px" role="img" aria-label="Presenter at board icon"></div>
  <div class="icon navy" style="left:1109px" role="img" aria-label="Follow up session icon"></div>

  <div class="tab grey" style="left:22px">1</div>
  <div class="step grey" style="left:22px">New Project Identified</div>
  <div class="tab blue" style="left:141px">2</div>
  <div class="step blue" style="left:141px">Governance Meeting</div>
  <div class="tab grey" style="left:260px">3</div>
  <div class="step grey" style="left:260px">Separate Project Meetings as needed</div>
  <div class="tab blue" style="left:379px">4</div>
  <div class="step blue" style="left:379px">Governance Meeting</div>
  <div class="tab blue" style="left:498px">5</div>
  <div class="step blue" style="left:498px">Weekly Center leader Meeting
    <span class="mark" style="left:62px;top:10px">*</span>
    <span class="note" style="top:154px"><span class="star">*</span> to collect feedback</span></div>
  <div class="tab blue" style="left:618px">6</div>
  <div class="step blue" style="left:618px">Field Advisory Panel</div>
  <div class="tab blue" style="left:737px">7</div>
  <div class="step blue" style="left:737px">Weekly Center Leader Meeting
    <span class="mark" style="left:64px;top:10px">*</span>
    <span class="note" style="top:154px"><span class="star">*</span> Center Planning and Specific execution details</span></div>
  <div class="tab navy" style="left:856px">8</div>
  <div class="step navy" style="left:856px">Monday Memo</div>
  <div class="tab navy" style="left:975px">9</div>
  <div class="step navy" style="left:975px">Daily Digest</div>
  <div class="tab navy" style="left:1095px">10</div>
  <div class="step navy" style="left:1095px">Follow Up Guide</div>

  <svg class="arrow" style="left:111px" viewBox="0 0 22 24"><polygon points="0,0 12,0 22,12 12,24 0,24 0,0" fill="#3a4150"/></svg>
  <svg class="arrow" style="left:230px" viewBox="0 0 22 24"><polygon points="0,0 12,0 22,12 12,24 0,24" fill="#3a4150"/></svg>
  <svg class="arrow" style="left:349px" viewBox="0 0 22 24"><polygon points="0,0 12,0 22,12 12,24 0,24" fill="#3a4150"/></svg>
  <svg class="arrow" style="left:469px" viewBox="0 0 22 24"><polygon points="0,0 12,0 22,12 12,24 0,24" fill="#3a4150"/></svg>
  <svg class="arrow" style="left:588px" viewBox="0 0 22 24"><polygon points="0,0 12,0 22,12 12,24 0,24" fill="#3a4150"/></svg>
  <svg class="arrow" style="left:707px" viewBox="0 0 22 24"><polygon points="0,0 12,0 22,12 12,24 0,24" fill="#3a4150"/></svg>
  <svg class="arrow" style="left:826px" viewBox="0 0 22 24"><polygon points="0,0 12,0 22,12 12,24 0,24" fill="#3a4150"/></svg>
  <svg class="arrow" style="left:945px" viewBox="0 0 22 24"><polygon points="0,0 12,0 22,12 12,24 0,24" fill="#3a4150"/></svg>
  <svg class="arrow" style="left:1065px" viewBox="0 0 22 24"><polygon points="0,0 12,0 22,12 12,24 0,24" fill="#3a4150"/></svg>

  <div class="divider"></div>

  <section class="notes">
    <div class="item">2 - <span class="label">Purpose:</span> Go/No Go Decision<br>
      <span class="overview"><span class="label">Overview:</span> Project Owner presents one pager to Sr Leadership. Based on Business Value, and Capacity a Go/No Go Decision is made.</span></div>
    <div class="item">4 - <span class="label">Purpose:</span> Report out on Milestone status and Key Decision Points<br>
      <span class="overview"><span class="label">Overview:</span> Project Owner presents milestones and feedback/approvals during key decision points.</span></div>
    <div class="item">5 - <span class="label">Purpose:</span> Introduce Project &amp; gather Center Leader Feedback<br>
      <span class="overview"><span class="label">Overview:</span> Project Owner provides overview of project, collects center leader feedback.</span></div>
    <div class="item">6 - <span class="label">Purpose:</span> Collect Center Staff Feedback<br>
      <span class="overview"><span class="label">Overview:</span> Project Owner presents project and collect Center Staff Feedback</span></div>
    <div class="item">7 - <span class="label">Purpose:</span> Provide Center Leaders with Implementation Details<br>
      <span class="overview" style="padding-left:16px"><span class="label">Overview:</span> Project Owner presents project and implementation details to ensure Center Leaders are prepared.</span></div>
  </section>

  <section class="phases">
    <div class="phase" style="top:15px">Planning &amp; Design Phase: 1 to 6</div>
    <div class="phase" style="top:82px">Prepare Phase: 7 to 9</div>
    <div class="phase" style="top:145px">Follow up &amp; Evaluate Phase: 10</div>
    <div class="phase-icon" style="top:8px" role="img" aria-label="Drafting tools icon"></div>
    <div class="phase-icon" style="top:75px" role="img" aria-label="Planning board icon"></div>
    <div class="phase-icon" style="top:138px" role="img" aria-label="Evaluation tools icon"></div>
  </section>

  <section class="legend">
    <div class="key meetings">Meetings</div>
    <div class="key tools">Emails/Tools</div>
  </section>
</body>
</html>
```